Lumaru Health Care Website - this is a website for a medical practice

This is a medical practice and would like my logo to be presented. I have attached a copy of some copy that should give you an idea of what my practice is about. My practice will be seeing Medicare patients in their homes. No coming to the office for a visit. I listen to my patients and provide individualized care. The name "Lumaru" means star in Hawaiʻian and want the patient to feel that they are the main focus of my practice.

Target Market(s)

Medicare patients

Industry/Entity Type

medical

Coding

Coded - Design and coding required

Number of Pages Required

2 page

Font styles to use
Sans Serif

Colors
00AB8E
00BBA5
67D7C9
C6EFE9
E9F9F6

Requirements
Must have
• feeling that I care about each patient and that I will do my very best to keep them as healthy as possible, that the Hawaiʻian culture is represented. Simple and easy to navigate for someone who isnʻt tech savvy. In normal conversational language.
Nice to have
• The elderly in Hawaiʻi are called Kapuna and they are revered. I would like to convey that.
Should not have
• Medical jargon

```html
<!DOCTYPE html>
<html lang="en">
<head>
<meta charset="utf-8">
<title>Lumaru Healthcare – Bringing Health to Your Home</title>
<link href="https://fonts.googleapis.com/css2?family=Nunito+Sans:wght@400;600;700;800&family=Open+Sans:wght@400;600;700&display=swap" rel="stylesheet">
<style>
:root{
  --teal:#00AB8E;
  --teal-2:#00BBA5;
  --teal-3:#67D7C9;
  --teal-4:#C6EFE9;
  --teal-5:#E9F9F6;
  --navy:#1f3d6b;
  --navy-card:#2c4f86;
  --ink:#23324a;
  --muted:#6b7280;
  --grey-bg:#f1f3f6;
  --dark:#222325;
  --footer:#1d2440;
  --footer-bar:#2b3d6a;
  --white:#ffffff;
}
*{box-sizing:border-box;margin:0;padding:0}
html,body{width:1200px;height:5121px;overflow:hidden}
body{position:relative;font-family:"Open Sans",sans-serif;color:var(--ink);background:var(--white)}
h1,h2,h3,h4{font-family:"Nunito Sans",sans-serif}
.abs{position:absolute}
.photo{position:absolute}
.label{font-size:15px;color:var(--teal);font-family:"Nunito Sans",sans-serif;font-weight:600}
.title{font-size:34px;color:var(--navy);font-weight:700;line-height:1.3}
.center{text-align:center;left:0;width:1200px}
.body-text{font-size:12.5px;line-height:22px;color:var(--muted)}
.btn{position:absolute;background:var(--teal);color:#fff;font-size:10px;font-weight:700;display:flex;align-items:center;justify-content:center;gap:14px;border-radius:3px;font-family:"Nunito Sans",sans-serif;letter-spacing:.3px}
.btn svg{width:14px;height:14px}

/* hero */
.hero{position:absolute;left:0;top:0;width:1200px;height:680px;overflow:hidden}
.hero-photo{left:0;top:0;width:1200px;height:680px;background:linear-gradient(100deg,#8c8d88 0%,#6e7b7c 30%,#a6a59c 55%,#c8c2b4 75%,#7d7466 100%)}
.hero-shade{left:0;top:0;width:1200px;height:680px;background:linear-gradient(90deg,rgba(20,30,40,.35),rgba(20,30,40,.05) 60%)}
.logo{position:absolute;font-family:"Nunito Sans",sans-serif;font-weight:600;line-height:1.05}
.hero .logo{left:118px;top:10px;color:#fff;font-size:24px;text-align:center}
.nav{left:340px;top:0;width:520px;height:46px;background:#fff;border-radius:0 0 22px 22px;display:flex;justify-content:space-around;align-items:center;padding:0 30px;font-size:10px;font-weight:600;color:var(--navy);font-family:"Nunito Sans",sans-serif}
.nav span.active{position:relative}
.nav span.active::before{content:"";position:absolute;left:0;right:0;top:-15px;height:2px;background:var(--teal)}
.hero-phone{left:905px;top:14px;color:#fff;display:flex;gap:8px;align-items:center}
.hero-phone small{display:block;font-size:7px;opacity:.85}
.hero-phone b{font-size:10px;font-weight:600}
.socials{left:48px;top:270px;display:flex;flex-direction:column;gap:14px}
.socials i{display:block;width:28px;height:28px;border:1.5px solid #fff;border-radius:50%}
.socials i.on{background:var(--teal-2);border-color:var(--teal-2)}
.hero h1{left:228px;top:205px;color:#fff;font-size:46px;line-height:58px;font-weight:700}
.hero p{left:234px;top:342px;color:#fff;font-size:12.5px;line-height:22px}

/* about */
.about-img-main{left:573px;top:790px;width:524px;height:402px;background:linear-gradient(135deg,#d9d2c6,#b9a98f 45%,#3b5a86 80%,#2d4870)}
.about-img-a{left:122px;top:1098px;width:325px;height:222px;background:linear-gradient(135deg,#4a7fa5,#9fb6c4 50%,#c9ced2)}
.about-img-b{left:475px;top:1098px;width:325px;height:222px;background:linear-gradient(135deg,#5f6770,#8b8e8f 50%,#b9b4aa)}

/* services */
.services{left:0;top:1408px;width:1200px;height:720px;background:var(--grey-bg)}
.svc-photo{position:absolute;width:320px;height:400px}
.svc-card{position:absolute;width:265px;height:227px;background:var(--navy-card);color:#fff;text-align:center;padding-top:38px}
.svc-card h3{font-size:24px;font-weight:600;line-height:33px}
.svc-card p{font-size:12px;line-height:21px;margin:12px 26px 0;opacity:.9}
.svc-card .go{width:32px;height:32px;border:2px solid #fff;border-radius:50%;margin:14px auto 0;display:flex;align-items:center;justify-content:center}

/* why */
.why-navy{left:0;top:2178px;width:600px;height:496px;background:var(--navy)}
.why-teal{left:600px;top:2145px;width:600px;height:562px;background:linear-gradient(135deg,var(--teal-2),var(--teal))}
.why-frame{left:560px;top:2238px;width:475px;height:387px;border:3px solid #fff}
.why-tab{left:1035px;top:2238px;width:38px;height:150px;background:#fff;display:flex;align-items:center;justify-content:center}
.why-tab span{transform:rotate(-90deg);white-space:nowrap;font-size:12px;font-weight:600;color:var(--navy);text-decoration:underline}
.why-item{position:absolute;left:650px;display:flex;gap:22px;color:#fff;width:360px}
.why-item .ic{flex:none;width:66px;height:66px;border:2px solid rgba(255,255,255,.85);border-radius:50%;display:flex;align-items:center;justify-content:center}
.why-item h4{font-size:17px;font-weight:600;margin-top:6px}
.why-item p{font-size:12px;line-height:22px;opacity:.95}

/* gallery */
.vid-side{position:absolute;top:2908px;width:232px;height:372px}
.vid-main{left:355px;top:2908px;width:495px;height:372px;background:linear-gradient(160deg,#6f7e86,#4d6672 50%,#3a5a6a)}
.vid-main .play{position:absolute;left:204px;top:150px;width:74px;height:74px;border-radius:50%;background:var(--teal-2);display:flex;align-items:center;justify-content:center}
.vid-main p{position:absolute;left:38px;top:296px;color:#fff;font-size:16px;line-height:24px}

/* quote */
.quote-dark{left:0;top:3360px;width:1200px;height:580px;background:var(--dark)}
.quote-teal{left:0;top:3360px;width:455px;height:580px;background:linear-gradient(160deg,var(--teal-2),var(--teal))}
.quote-people{left:130px;top:3400px;width:430px;height:540px;background:linear-gradient(180deg,#2a2e36,#1e2230 60%,#2b2f3a);border-radius:180px 180px 0 0}
.quote-vert{left:40px;top:3650px;transform:rotate(-90deg);transform-origin:center;white-space:nowrap;color:#fff;font-size:34px;font-weight:700;font-family:"Nunito Sans",sans-serif;width:0;display:flex;justify-content:center}
.field{position:absolute;border:1.5px solid #8a8c90;border-radius:3px;color:#b8b9bb;font-size:9px;padding:9px 14px}

/* testimonials */
.t-side{position:absolute;top:4148px;width:137px;height:289px}
.t-card{left:487px;top:4148px;width:451px;height:289px;background:#fff;box-shadow:0 4px 20px rgba(20,30,60,.08);padding:42px 42px 0 44px}

/* footer */
.footer{left:0;top:4540px;width:1200px;height:535px;background:var(--footer);color:#fff}
.f-col h4{font-size:20px;font-weight:700;margin-bottom:16px}
.f-col h4::after{content:"";display:block;width:46px;height:3px;background:var(--teal);margin-top:12px}
.links{display:grid;grid-template-columns:165px 120px;row-gap:14px;font-size:13px}
.links span::before{content:"›";margin-right:10px}
.fbar{left:85px;top:4975px;width:1027px;height:86px;background:var(--footer-bar);display:flex;align-items:center}
.fbar div{flex:1;display:flex;align-items:center;gap:20px;padding-left:30px;font-size:14px;color:#fff}
.fbar div+div{border-left:1px solid rgba(255,255,255,.2)}
.fbar b{display:block;font-size:14px}
.legal{left:0;top:5075px;width:1200px;height:46px;background:#fff;font-size:11px;color:#3a4253}
</style>
</head>
<body>

<!-- HERO -->
<section class="hero">
  <div class="photo hero-photo" role="img" aria-label="Nurse and caregivers reviewing a patient's care on a tablet"></div>
  <div class="photo hero-shade"></div>
  <div class="logo">Lumaru<br><span style="font-weight:400">Healthcare</span></div>
  <nav class="abs nav">
    <span class="active">HOME</span><span>ABOUT</span><span>SERVICES</span><span>CASES</span><span>BLOG</span><span>CONTACT+</span>
  </nav>
  <div class="abs hero-phone">
    <svg width="18" height="18" viewBox="0 0 24 24" fill="none" stroke="#fff" stroke-width="2"><path d="M22 16.9v3a2 2 0 0 1-2.2 2 19.8 19.8 0 0 1-8.6-3.1 19.5 19.5 0 0 1-6-6A19.8 19.8 0 0 1 2.1 4.2 2 2 0 0 1 4.1 2h3a2 2 0 0 1 2 1.7c.1.9.4 1.8.7 2.7a2 2 0 0 1-.5 2.1L8 9.8a16 16 0 0 0 6 6l1.3-1.3a2 2 0 0 1 2.1-.5c.9.3 1.8.6 2.7.7a2 2 0 0 1 1.7 2z"/></svg>
    <div><small>Have Any Questions?</small><b>+01 3 5550 1942</b></div>
  </div>
  <div class="abs socials"><i></i><i></i><i class="on"></i><i></i></div>
  <h1 class="abs">Bringing Health to<br>Your Home</h1>
  <p class="abs">Lorem ipsum dolor sit amet, consectetur adipiscing elit, sed<br>do eiusmod tempor incididunt ut labore et dolore magna aliqua.</p>
  <div class="btn" style="left:234px;top:402px;width:152px;height:44px">READ MORE
    <svg viewBox="0 0 24 24" fill="none" stroke="#fff" stroke-width="2.4"><path d="M5 12h14M13 6l6 6-6 6"/></svg></div>
  <svg class="abs" style="left:0;top:600px" width="1200" height="80" viewBox="0 0 1200 80"><path d="M460 8 Q420 8 405 40 Q392 78 360 80 L1200 80 L1200 8 Z" fill="#fff"/></svg>
</section>

<!-- ABOUT -->
<section>
  <div class="abs label" style="left:118px;top:820px">About Us</div>
  <h2 class="abs title" style="left:118px;top:840px;width:440px">Holistic Care, Heartfelt Connections</h2>
  <p class="abs body-text" style="left:124px;top:938px;width:440px">Lorem ipsum dolor sit amet, consectetur adipiscing elit, sed do eiusmod tempor incididunt ut labore et dolore magna aliqua. Ut enim ad minim veniam, q</p>
  <p class="abs" style="left:124px;top:1022px;color:var(--teal);font-size:16px">"Empowering Elderly, Enriching Lives"</p>
  <div class="photo about-img-main" role="img" aria-label="Smiling kūpuna with a cane beside a caregiver in scrubs"></div>
  <div class="abs" style="left:1119px;top:793px;width:3px;height:130px;background:var(--teal-2)"></div>
  <div class="abs" style="left:820px;top:1208px;width:275px;height:2px;background:linear-gradient(90deg,var(--teal-2),transparent)"></div>
  <div class="photo about-img-a" role="img" aria-label="Caregiver sitting with an elderly woman"></div>
  <div class="photo about-img-b" role="img" aria-label="Caregiver helping an elder walk with a cane"></div>
</section>

<!-- SERVICES -->
<section class="abs services">
  <div class="abs label center" style="top:62px">Our Latest Services</div>
  <h2 class="abs title center" style="top:92px">Services We Provide</h2>

  <div class="svc-photo" style="left:95px;top:188px;background:linear-gradient(150deg,#d8dde2,#9fb0c2 60%,#5c7ea3)" role="img" aria-label="Nurse caring for an elderly man at home"></div>
  <div class="svc-card" style="left:121px;top:402px"><h3>Home<br>Care</h3><p>Lorem ipsum dolor sit amet, ae consectetur adipiscing</p>
    <div class="go"><svg width="14" height="14" viewBox="0 0 24 24" fill="none" stroke="#fff" stroke-width="3"><path d="M9 5l7 7-7 7"/></svg></div></div>

  <div class="svc-photo" style="left:440px;top:229px;background:linear-gradient(160deg,#c8a27a,#8a6a4a 50%,#3d4a5a)" role="img" aria-label="Elder seated in a wheelchair receiving support"></div>
  <div class="svc-card" style="left:467px;top:188px"><h3>Palliative<br>Care</h3><p>Lorem ipsum dolor sit amet, ae consectetur adipiscing</p>
    <div class="go"><svg width="14" height="14" viewBox="0 0 24 24" fill="none" stroke="#fff" stroke-width="3"><path d="M9 5l7 7-7 7"/></svg></div></div>

  <div class="svc-photo" style="left:788px;top:188px;background:linear-gradient(150deg,#8a9a78,#6e8a6a 40%,#4f7aa5)" role="img" aria-label="Caregiver and elder woman walking outdoors"></div>
  <div class="svc-card" style="left:815px;top:402px"><h3>Hospice<br>Care</h3><p>Lorem ipsum dolor sit amet, ae consectetur adipiscing</p>
    <div class="go"><svg width="14" height="14" viewBox="0 0 24 24" fill="none" stroke="#fff" stroke-width="3"><path d="M9 5l7 7-7 7"/></svg></div></div>
</section>

<!-- WHY US -->
<section>
  <div class="photo why-navy"></div>
  <div class="photo why-teal" role="img" aria-label="Caregiver and patient, softly tinted in teal"></div>
  <div class="abs label" style="left:118px;top:2280px;color:var(--teal-2);font-size:14px">Why we are the Best</div>
  <h2 class="abs" style="left:118px;top:2302px;color:#fff;font-size:34px;line-height:45px;font-weight:700">Home is Where<br>Health Begins</h2>
  <p class="abs" style="left:124px;top:2414px;width:430px;color:#fff;font-size:12.5px;line-height:22px">Lorem ipsum dolor sit amet, consectetur adipiscing elit, sed do eiusmod tempor incididunt ut labore et dolore magna aliqua. Ut enim ad minim veniam, q</p>
  <div class="btn" style="left:128px;top:2530px;width:150px;height:44px">READ MORE
    <svg viewBox="0 0 24 24" fill="none" stroke="#fff" stroke-width="2.4"><path d="M5 12h14M13 6l6 6-6 6"/></svg></div>
  <div class="abs why-frame"></div>
  <div class="abs why-tab"><span>GET A QUOTE</span></div>

  <div class="why-item" style="top:2272px"><div class="ic">
    <svg width="30" height="30" viewBox="0 0 24 24" fill="none" stroke="#fff" stroke-width="1.6"><circle cx="12" cy="7" r="3.5"/><path d="M5 20c0-4 3-6.5 7-6.5s7 2.5 7 6.5"/></svg></div>
    <div><h4>Empathetic Staff</h4><p>Lorem ipsum dolor sit amet, consecte tur adipiscing elit, sed do</p></div></div>
  <div class="why-item" style="top:2385px"><div class="ic">
    <svg width="30" height="30" viewBox="0 0 24 24" fill="none" stroke="#fff" stroke-width="1.6"><path d="M12 3l2.7 5.6 6.1.9-4.4 4.3 1 6.1L12 17l-5.4 2.9 1-6.1L3.2 9.5l6.1-.9z"/></svg></div>
    <div><h4>Client-Centric</h4><p>Lorem ipsum dolor sit amet, consecte tur adipiscing elit, sed do</p></div></div>
  <div class="why-item" style="top:2497px"><div class="ic">
    <svg width="30" height="30" viewBox="0 0 24 24" fill="none" stroke="#fff" stroke-width="1.6"><circle cx="12" cy="12" r="8"/><path d="M12 7v5l3 3"/></svg></div>
    <div><h4>Professionalism</h4><p>Lorem ipsum dolor sit amet, consecte tur adipiscing elit, sed do</p></div></div>
</section>

<!-- GALLERY -->
<section>
  <div class="abs label center" style="top:2780px">Gallery</div>
  <h2 class="abs title center" style="top:2808px">Watch Our Videos</h2>
  <svg class="abs" style="left:95px;top:2908px" width="232" height="372"><polygon points="0,30 232,0 232,372 0,342" fill="#c9d3dc"/></svg>
  <div class="vid-side" style="left:95px;clip-path:polygon(0 8%,100% 0,100% 100%,0 92%);background:linear-gradient(135deg,#e3e8ec,#aebccb 60%,#7f97b0)" role="img" aria-label="Nurse reviewing notes with a patient"></div>
  <div class="photo vid-main" role="img" aria-label="Caregiver visiting an elderly woman on her couch">
    <div class="play"><svg width="30" height="30" viewBox="0 0 24 24"><path d="M7 4l13 8-13 8z" fill="#fff"/></svg></div>
    <p>Lorem ipsum dolor sit amet, consecteturipsum<br>dolor sit amet, consectetur</p>
  </div>
  <div class="vid-side" style="left:877px;clip-path:polygon(0 0,100% 8%,100% 92%,0 100%);background:linear-gradient(135deg,#8fb1c4,#b5c9d4 50%,#d7dfe4)" role="img" aria-label="Nurse embracing a smiling elder"></div>
</section>

<!-- QUOTE -->
<section>
  <div class="photo quote-dark"></div>
  <div class="photo quote-teal"></div>
  <div class="photo quote-people" role="img" aria-label="Two smiling care coordinators standing back to back"></div>
  <div class="abs quote-vert" style="left:72px">GET A FREE QUOTE</div>
  <div class="abs" style="left:0;top:3842px;width:140px;height:2px;background:#fff"></div>
  <div class="abs" style="left:818px;top:3842px;width:382px;height:2px;background:#fff"></div>
  <div class="abs" style="left:818px;top:3442px;width:382px;height:1px;background:#777"></div>
  <div class="abs label" style="left:630px;top:3434px;color:var(--teal-2)">Contact Us</div>
  <h2 class="abs" style="left:630px;top:3458px;color:#fff;font-size:32px;font-weight:700">GET A FREE QUOTE</h2>
  <div class="field" style="left:635px;top:3545px;width:203px;height:35px">Your Name</div>
  <div class="field" style="left:870px;top:3545px;width:203px;height:35px">Phone Number</div>
  <div class="field" style="left:635px;top:3605px;width:203px;height:35px">Email Address</div>
  <div class="field" style="left:870px;top:3605px;width:203px;height:35px">Location</div>
  <div class="field" style="left:635px;top:3655px;width:438px;height:135px">Your Message</div>
  <div class="btn" style="left:628px;top:3825px;width:150px;height:44px">READ MORE
    <svg viewBox="0 0 24 24" fill="none" stroke="#fff" stroke-width="2.4"><path d="M5 12h14M13 6l6 6-6 6"/></svg></div>
</section>

<!-- TESTIMONIALS -->
<section>
  <div class="abs label center" style="top:4038px">Our Testimonials</div>
  <h2 class="abs title center" style="top:4064px">Client Reviews</h2>
  <div class="t-side" style="left:100px;background:linear-gradient(160deg,#3f5f93,#2a4c80)" role="img" aria-label="Previous client portrait">
    <svg style="position:absolute;left:50px;top:127px" width="36" height="36" viewBox="0 0 24 24" fill="none" stroke="#fff" stroke-width="2"><path d="M19 12H5M11 6l-6 6 6 6"/></svg></div>
  <div class="photo" style="left:262px;top:4148px;width:225px;height:289px;background:linear-gradient(160deg,#e6e6e4,#b4b6b8 60%,#7c8088)" role="img" aria-label="Portrait of a smiling client"></div>
  <div class="abs t-card">
    <svg width="30" height="22" viewBox="0 0 30 22"><path d="M0 22V12Q0 2 11 0v5q-5 1-5 7h5v10zM17 22V12q0-10 11-12v5q-5 1-5 7h5v10z" fill="var(--navy)"/></svg>
    <p class="body-text" style="font-size:12px;margin-top:18px">Lorem ipsum dolor sit amet, consectetur adipiscing elit, sed do eiusmod tempor incididunt ut labore et dolore magna aliqua. Ut enim ad minim veniam, qdkldunt ut labore et dolore magna aliqua.</p>
    <div style="display:flex;justify-content:space-between;align-items:flex-end;margin-top:24px">
      <div><b style="font-size:16px;font-weight:600;color:#222">Malia Kealoha</b><div style="font-size:9px;color:#888">Chairperson</div></div>
      <div style="color:#f0a43a;font-size:13px;letter-spacing:2px">★★★★★</div>
    </div>
  </div>
  <div class="t-side" style="left:963px;background:linear-gradient(160deg,#3f5f93,#2a4c80)" role="img" aria-label="Next client portrait">
    <svg style="position:absolute;left:50px;top:127px" width="36" height="36" viewBox="0 0 24 24" fill="none" stroke="#fff" stroke-width="2"><path d="M5 12h14M13 6l6 6-6 6"/></svg></div>
</section>

<!-- FOOTER -->
<footer class="abs footer">
  <div class="logo" style="left:80px;top:62px;color:var(--teal);font-size:36px;text-align:center;font-weight:400">Lumaru<br>Healthcare</div>
  <div class="abs" style="left:82px;top:160px;font-size:17px;font-weight:700">808-555-0175</div>
  <div class="abs" style="left:84px;top:186px;font-size:13px;font-weight:700">Call for free consultation</div>
  <p class="abs" style="left:84px;top:218px;width:280px;font-size:12px;line-height:22px">Lorem ipsum dolor sit amet, consectet sed do eiusmod tempor incididunt ut la magna aliqua. Ut enim</p>
  <div class="abs" style="left:84px;top:300px;font-size:14px;font-weight:700">Read more &nbsp;›</div>

  <div class="abs f-col" style="left:438px;top:100px"><h4>Useful Links</h4>
    <div class="links"><span>About Company</span><span>Services</span><span>Leadership</span><span>Industries</span><span>Blog Post</span><span>Feedback</span><span>FAQ'S</span><span>Partners</span><span>Certification</span><span>Pricing</span><span>Testimonials</span><span>Contct</span></div></div>

  <div class="abs f-col" style="left:788px;top:100px;width:320px"><h4>Newsletter</h4>
    <p style="font-size:12px;line-height:26px;margin-top:20px">Dont miss to subscribe to our news feeds, kindly fill the form below</p>
    <div style="margin-top:20px;display:flex;height:48px;background:#161c34;border-radius:3px">
      <span style="flex:1;font-size:12px;padding:15px 24px">Your Email Address</span>
      <span style="width:50px;background:var(--teal);border-radius:0 24px 24px 0;display:flex;align-items:center;justify-content:center"><svg width="18" height="18" viewBox="0 0 24 24" fill="none" stroke="#fff" stroke-width="3"><path d="M9 5l7 7-7 7"/></svg></span>
    </div></div>
</footer>
<div class="abs fbar">
  <div><svg width="30" height="30" viewBox="0 0 24 24" fill="none" stroke="var(--teal-2)" stroke-width="1.6"><path d="M12 22s7-6.5 7-12a7 7 0 0 0-14 0c0 5.5 7 12 7 12z"/><circle cx="12" cy="10" r="2.5"/></svg><span><b>Location</b>246 &nbsp;Rd, Country</span></div>
  <div><svg width="30" height="30" viewBox="0 0 24 24" fill="none" stroke="var(--teal-2)" stroke-width="1.6"><rect x="3" y="5" width="18" height="14" rx="1"/><path d="M7 10h10M7 14h6"/></svg><span><b>Mail us</b>care@lumaru-health.example</span></div>
  <div><svg width="30" height="30" viewBox="0 0 24 24" fill="none" stroke="var(--teal-2)" stroke-width="1.6"><path d="M22 2L11 13M22 2l-7 20-4-9-9-4z"/></svg><span><b>Office hrs</b>9.00am to 7.00pm (Mon-Sat)</span></div>
</div>
<div class="abs" style="left:1125px;top:5000px;width:47px;height:46px;background:var(--teal);display:flex;align-items:center;justify-content:center">
  <svg width="20" height="20" viewBox="0 0 24 24" fill="none" stroke="#fff" stroke-width="3"><path d="M5 15l7-7 7 7"/></svg></div>
<div class="abs legal">
  <span class="abs" style="left:85px;top:15px">Lumaru Health</span>
  <span class="abs" style="left:801px;top:15px;word-spacing:2px">Privacy Policy &nbsp;&nbsp;&nbsp;&nbsp; Terms &amp; Conditions &nbsp;&nbsp;&nbsp;&nbsp; Site Map</span>
</div>

</body>
</html>
```